Northpeak Billing needs a business card design

We need a business card design for a medical billing service, located in Anchorage, AK. We provide medical claims billing and management to Alaskan medical practices/clinics. We would like to see designs that depict Alaskan Mountain Ranges, or water features, or trees. An outdoorsy feel, perhaps. Not exactly sure.

```html
<!DOCTYPE html>
<html lang="en">
<head>
<meta charset="utf-8">
<title>Northpeak Billing – Business Card</title>
<link rel="stylesheet" href="https://fonts.googleapis.com/css2?family=Gelasio:wght@400;700&family=Questrial&display=swap">
<style>
  :root {
    --bg: #e9e7ea;
    --card: #ffffff;
    --ink: #1b1b1b;
    --navy: #2a2f8f;
    --red: #e8212b;
    --shadow: rgba(40, 20, 40, 0.18);
  }
  html, body {
    margin: 0;
    padding: 0;
    width: 1200px;
    height: 800px;
    overflow: hidden;
    background: var(--bg);
  }
  .canvas {
    position: relative;
    width: 1200px;
    height: 800px;
    display: flex;
    align-items: center;
    justify-content: center;
    gap: 60px;
  }
  .card {
    position: relative;
    width: 525px;
    height: 300px;
    background: var(--card);
    box-shadow: 0 10px 30px var(--shadow);
    overflow: hidden;
  }
  .brand {
    font-family: "Gelasio", Georgia, serif;
    font-weight: 700;
    color: var(--navy);
    display: flex;
    align-items: center;
    gap: 12px;
    line-height: 1.05;
    margin: 0;
  }
  .brand-dot {
    flex: none;
    border-radius: 50%;
    background: var(--navy);
  }
  /* back side */
  .card-back .brand {
    position: absolute;
    left: 50%;
    top: 50%;
    transform: translate(-50%, -50%);
    font-size: 40px;
  }
  .card-back .brand-dot { width: 28px; height: 28px; }

  /* front side */
  .card-front .brand {
    position: absolute;
    left: 34px;
    top: 72px;
    width: 215px;
    font-size: 31px;
  }
  .card-front .brand-dot { width: 22px; height: 22px; }
  .divider {
    position: absolute;
    left: 268px;
    top: 58px;
    width: 1px;
    height: 150px;
    background: var(--ink);
  }
  .contact {
    position: absolute;
    left: 288px;
    top: 58px;
    width: 225px;
    color: var(--ink);
  }
  .contact-name {
    font-family: "Gelasio", Georgia, serif;
    font-weight: 700;
    font-size: 21px;
    line-height: 1.2;
    margin: 0;
  }
  .contact-title {
    font-family: "Questrial", Arial, sans-serif;
    font-size: 13px;
    line-height: 1.2;
    margin: 3px 0 12px;
  }
  .contact-list {
    list-style: none;
    margin: 0;
    padding: 0;
    font-family: "Questrial", Arial, sans-serif;
    font-size: 14px;
  }
  .contact-list li {
    display: flex;
    align-items: center;
    gap: 8px;
    height: 22px;
    white-space: nowrap;
  }
  .icon { width: 14px; height: 14px; flex: none; }
  .tagline-band {
    position: absolute;
    left: 0;
    bottom: 0;
    width: 100%;
    height: 36px;
    background: var(--red);
    color: #fff;
    font-family: "Questrial", Arial, sans-serif;
    font-size: 13.5px;
    display: flex;
    align-items: center;
    padding-left: 22px;
    box-sizing: border-box;
    white-space: nowrap;
  }
</style>
</head>
<body>
<main class="canvas">
  <section class="card card-back" aria-label="Card back">
    <p class="brand"><span class="brand-dot"></span><span>Northpeak<br>Billing</span></p>
  </section>

  <section class="card card-front" aria-label="Card front">
    <p class="brand"><span class="brand-dot"></span><span>Northpeak<br>Billing</span></p>
    <div class="divider"></div>
    <div class="contact">
      <p class="contact-name">Your name here</p>
      <p class="contact-title">Title here</p>
      <ul class="contact-list">
        <li>
          <svg class="icon" viewBox="0 0 14 14"><rect width="14" height="14" rx="2" fill="var(--red)"/><rect x="4" y="3" width="6" height="8" fill="none" stroke="#fff" stroke-width="1.3"/><line x1="6" y1="5" x2="8" y2="5" stroke="#fff"/><line x1="6" y1="7" x2="8" y2="7" stroke="#fff"/></svg>
          (555)014-2207
        </li>
        <li>
          <svg class="icon" viewBox="0 0 14 14"><rect width="14" height="14" rx="2" fill="var(--red)"/><path d="M4.5 3.5c-1 1 -1 3 1 5s4 2 5 1l-1.5-1.5-1 .8c-.8-.3-1.8-1.3-2.1-2.1l.8-1z" fill="#fff"/></svg>
          (555)018-7160
        </li>
        <li>
          <svg class="icon" viewBox="0 0 14 14"><rect width="14" height="14" rx="2" fill="var(--red)"/><rect x="3" y="4" width="8" height="6" fill="none" stroke="#fff" stroke-width="1.2"/><path d="M3 4l4 3.5 4-3.5" fill="none" stroke="#fff" stroke-width="1.2"/></svg>
          hello@northpeakbilling.com
        </li>
        <li>
          <svg class="icon" viewBox="0 0 14 14"><rect width="14" height="14" rx="2" fill="var(--red)"/><circle cx="7" cy="7" r="4" fill="none" stroke="#fff" stroke-width="1.2"/><line x1="3" y1="7" x2="11" y2="7" stroke="#fff"/><ellipse cx="7" cy="7" rx="1.8" ry="4" fill="none" stroke="#fff"/></svg>
          www.northpeakbilling.com
        </li>
      </ul>
    </div>
    <div class="tagline-band">Medical claims billing and management to Alaskan medical practices/clinics</div>
  </section>
</main>
</body>
</html>
```